Teachers workshop flyer

I need a flyer to inform schools of a workshop for teachers that empowers the teacher to help traumatised and disadvantaged students to engage in successful learning.

I am a teacher and educator and my info for the flyer is attached.

Target Market(s)

Principals and vice-principals who have stressed staff and students and they want things to be better in the school!

Industry/Entity Type

Teacher

```html
<!DOCTYPE html>
<html lang="en">
<head>
<meta charset="utf-8">
<title>Brain-based Strategies for Student Success</title>
<link href="https://fonts.googleapis.com/css2?family=Domine:wght@400;700&family=Work+Sans:wght@300&family=Barlow:wght@400;500&display=swap" rel="stylesheet">
<style>
  :root {
    --paper: #ffffff;
    --title: #f8b221;
    --title-ghost: #fde6b8;
    --mint: #4ff0b4;
    --ink: #3a3a3a;
    --accent: #ee3b4b;
    --photo-sky: #cfe6f2;
    --photo-warm: #e9b48c;
    --photo-teal: #5fc9b3;
    --photo-green: #7fb246;
  }
  * { margin: 0; padding: 0; box-sizing: border-box; }
  html, body { width: 927px; height: 1200px; overflow: hidden; background: var(--paper); }
  .flyer { position: relative; width: 927px; height: 1200px; background: var(--paper); }

  .hero-photo { position: absolute; left: 47px; top: 47px; }

  .title {
    position: absolute; left: 47px; top: 428px;
    font-family: "Domine", serif; font-weight: 700;
    font-size: 60px; line-height: 64px; letter-spacing: -0.5px;
  }
  .title .ghost { position: absolute; left: 20px; top: 14px; color: var(--title-ghost); white-space: nowrap; }
  .title .main { position: relative; color: var(--title); white-space: nowrap; }

  .intro {
    position: absolute; left: 47px; top: 726px; width: 545px;
    font-family: "Domine", serif; font-weight: 400;
    font-size: 24.5px; line-height: 30.3px; color: var(--mint);
  }
  .body-copy {
    position: absolute; left: 47px; top: 1000px; width: 540px;
    font-family: "Work Sans", sans-serif; font-weight: 300;
    font-size: 20.5px; line-height: 25.4px; color: var(--ink);
  }

  .sidebar {
    position: absolute; left: 614px; top: 602px; width: 272px;
    font-family: "Barlow", sans-serif; font-size: 13.6px; line-height: 17.4px; color: var(--ink);
  }
  .sidebar h2 { font-size: 13.6px; font-weight: 500; color: var(--accent); text-transform: uppercase; letter-spacing: 0.2px; }
  .sidebar p { margin-bottom: 17px; }
  .sidebar .contact strong { font-weight: 500; }
  .sidebar .link { color: var(--accent); }
  .sidebar section + section { margin-top: 26px; }
  .light-bulbs { list-style: none; }
  .light-bulbs li { position: relative; padding-left: 8px; }
  .light-bulbs li::before { content: "•"; position: absolute; left: 0; }
</style>
</head>
<body>
<main class="flyer">
  <svg class="hero-photo" width="831" height="526" viewBox="0 0 831 526" role="img" aria-label="Photo of smiling children leaning in together under a bright sky">
    <defs>
      <linearGradient id="photoTone" x1="0" y1="0" x2="1" y2="1">
        <stop offset="0" stop-color="var(--photo-warm)"/>
        <stop offset="0.45" stop-color="var(--photo-sky)"/>
        <stop offset="0.75" stop-color="var(--photo-teal)"/>
        <stop offset="1" stop-color="var(--photo-green)"/>
      </linearGradient>
    </defs>
    <path d="M0 0 H831 V526 H567 V360 H0 Z" fill="url(#photoTone)"/>
  </svg>

  <h1 class="title">
    <span class="ghost" aria-hidden="true">Brain-based<br>Strategies<br>for Student<br>Success</span>
    <span class="main">Brain-based<br>Strategies<br>for Student<br>Success</span>
  </h1>

  <p class="intro">Contemporary teaching is a highly complex role as increasing numbers of students attend school without the essential ‘self-skills’ to be truly ‘school-ready’ and successful. Instead these students often seek-out attention in ways that can disruptive in the classroom causing stress and frustration for teachers.</p>

  <p class="body-copy">Dan shows how and why the most effective strategies for these students are guided by a sound understanding of child-development and brain-development - especially where trauma has left lasting impacts. Teachers can learn how to build a student’s self-skills, without the teacher having to become a therapist!</p>

  <aside class="sidebar">
    <section>
      <h2>About the presenter</h2>
      <p>Daniel Whitford is a Melbourne-based therapist and educator with over twenty years experience working with adults and young people in the area of trauma and recovery. Dan’s seminars are engaging and practical since teachers need effective strategies that will immediately translate into classroom practice. Dan has trained here and overseas in the most effective behavior change strategies.</p>
      <p class="contact"><strong>Call 0400 123 456 for more information</strong> or to book Dan to come to your school: <span class="link">www.danielwhitford.com.au/ studentsuccess</span></p>
    </section>
    <section>
      <h2>Teacher feedback</h2>
      <p>“Dan was such an engaging and energetic presenter whom I enjoyed immensely. His presentation on the brain and take away strategies were so practical and meaningful. It was an invaluable session”.</p>
      <p>“My Light-bulb moments:</p>
      <ul class="light-bulbs">
        <li>I need to CONNECT – not correct – far more often.</li>
        <li>Seeing negative self-talk for what it is.</li>
        <li>Using far more ‘diversions’ in the avoidance loop”.</li>
      </ul>
    </section>
  </aside>
</main>
</body>
</html>
```